Manifesto

I want a manifesto with the following five manifestos for our Not for Profit

- We are a For-purpose organisation
- Every service we offer is free
- Every product we sell funds our services
- Every financial transaction is transparent
- Our service is for the greater good
- Our purpose is always to serve the people
- We are a for purpose organisation

Its to go with this website logo/look/feel www.brightlantern.co.nz

Two attachments:

1. I quite like this look/feel of a manifesto (see attached), I want something clean, professional but I also quite like either Retro modern look feel also like a fresh, and uplifting as its for sick people coming to see us and our funds where anyone buys a product are used for helping those who are sick with healing......so needs something conveyed that is fresh, uplifing yet professional.
2. This attachment is how I wrote this down when inspired of how I wanted Bright Lantern to operate. This is our values chart. It has to say

Also check out our website for our logo, look etc.. it doesnt have to be the same but red somewhere would link back to logo. www.brightlantern.co.nz .

```html
<!DOCTYPE html>
<html lang="en">
<head>
<meta charset="utf-8">
<title>Bright Lantern Manifesto</title>
<link rel="stylesheet" href="https://fonts.googleapis.com/css2?family=Lato:wght@300;400;700;900&family=Raleway:wght@100;200;300&family=Oswald:wght@400;500&family=Dancing+Script:wght@400;700&family=Roboto+Slab:wght@300;700;800&display=swap">
<style>
  :root {
    --red: #d9373b;
    --frame-grey: #6b6b6b;
    --ink: #1c1c1c;
    --ink-soft: #3a3a3a;
    --grey-mid: #8c8c8c;
    --grey-light: #c2c2c2;
    --panel-dark: #bdbdbd;
    --panel-light: #e3e3e3;
    --paper: #ffffff;
    --backdrop: #efefef;
  }
  * { margin: 0; padding: 0; box-sizing: border-box; }
  html, body { width: 1200px; height: 1103px; overflow: hidden; background: var(--backdrop); }
  .canvas { position: relative; width: 1200px; height: 1103px; overflow: hidden; background: var(--backdrop); }

  .manifesto { position: absolute; left: 391px; top: 38px; width: 418px; height: 1026px; }
  .manifesto__frame { position: absolute; inset: 0; width: 418px; height: 1026px; filter: drop-shadow(4px 5px 4px rgba(0,0,0,0.3)); }

  .line { position: absolute; left: 0; right: 0; text-align: center; line-height: 1; white-space: nowrap; }

  .brand { top: 50px; display: flex; justify-content: center; align-items: center; gap: 6px;
    font-family: "Lato", sans-serif; font-weight: 700; font-size: 17px; color: var(--red); }
  .brand__dot { width: 10px; height: 10px; border-radius: 50%; background: var(--red); }
  .brand__tagline { top: 72px; font-family: "Lato", sans-serif; font-size: 6px; letter-spacing: 1px; color: var(--grey-mid); }

  .swoosh { position: absolute; left: 40px; top: 104px; width: 338px; height: 20px; }

  .we-are { top: 155px; font-family: "Lato", sans-serif; font-weight: 300; font-size: 40px; color: var(--red); letter-spacing: 1px; }
  .band { position: absolute; top: 168px; width: 62px; height: 20px; background: var(--grey-light); }
  .band--left { left: 40px; clip-path: polygon(0 0, 100% 0, 100% 100%, 0 100%, 10% 50%); }
  .band--right { left: 316px; clip-path: polygon(0 0, 100% 0, 90% 50%, 100% 100%, 0 100%); }

  .heart { position: absolute; left: 181px; top: 206px; width: 56px; height: 50px; }
  .heart__letter { position: absolute; left: 0; right: 0; top: 212px; text-align: center;
    font-family: "Lato", sans-serif; font-weight: 300; font-size: 24px; color: var(--paper); line-height: 1; }

  .for-purpose { top: 268px; font-family: "Lato", sans-serif; font-weight: 900; font-size: 45px; color: var(--ink); }
  .organisation { top: 316px; font-family: "Lato", sans-serif; font-weight: 300; font-size: 40px; color: var(--ink); letter-spacing: 1px; }

  .dotted { position: absolute; left: 40px; width: 338px; border-top: 2px dotted var(--grey-light); }
  .dotted--upper { top: 362px; }
  .dotted--lower { top: 476px; }

  .every-large { top: 378px; font-family: "Raleway", sans-serif; font-weight: 100; font-size: 88px; color: var(--ink); letter-spacing: 8px; }

  .column { position: absolute; top: 484px; height: 232px; }
  .column--service { left: 40px; width: 172px; }
  .column--product { left: 218px; width: 158px; background: var(--paper); box-shadow: 0 0 3px rgba(0,0,0,0.12); }

  .service-title { top: 4px; font-family: "Lato", sans-serif; font-weight: 900; font-size: 29px; color: var(--ink-soft); }
  .we-offer { top: 34px; font-family: "Dancing Script", cursive; font-size: 18px; color: var(--ink-soft); }
  .ribbon { position: absolute; left: 16px; top: 55px; width: 140px; height: 28px; }
  .ribbon__word { top: 60px; font-family: "Lato", sans-serif; font-weight: 900; font-size: 18px; color: var(--red); }
  .rule { position: absolute; left: 0; right: 0; top: 94px; border-top: 2px solid var(--grey-light); }
  .every-band { position: absolute; left: 0; right: 0; top: 106px; height: 36px; background: var(--red);
    font-family: "Lato", sans-serif; font-weight: 900; font-size: 28px; color: var(--paper); text-align: center; line-height: 36px; }
  .financial { top: 146px; font-family: "Dancing Script", cursive; font-size: 30px; color: var(--grey-mid); }
  .transaction { top: 177px; font-family: "Lato", sans-serif; font-weight: 700; font-size: 12px; color: var(--grey-mid); letter-spacing: 1px; }
  .small-dot { position: absolute; left: 50%; width: 15px; height: 15px; margin-left: -7.5px; border-radius: 50%;
    background: var(--red); color: var(--paper); font-family: "Lato", sans-serif; font-size: 8px; font-weight: 700;
    line-height: 15px; text-align: center; }
  .column--service .small-dot { top: 193px; }
  .transparent { top: 212px; font-family: "Roboto Slab", serif; font-weight: 700; font-size: 15px; color: var(--ink-soft); }

  .product-title { top: 8px; font-family: "Lato", sans-serif; font-weight: 900; font-size: 25px; color: var(--red); letter-spacing: 1px; }
  .we-sell { top: 36px; font-family: "Dancing Script", cursive; font-weight: 700; font-size: 24px; color: var(--ink); }
  .funds { top: 72px; font-family: "Lato", sans-serif; font-weight: 300; font-size: 38px; color: var(--ink-soft); }
  .our-small { top: 110px; font-family: "Oswald", sans-serif; font-weight: 500; font-size: 38px; color: var(--ink-soft); }
  .services { top: 154px; font-family: "Oswald", sans-serif; font-weight: 400; font-size: 42px; color: var(--red); letter-spacing: -1px; }

  .chevron { position: absolute; left: 40px; top: 716px; width: 338px; height: 62px; }
  .our-divider { top: 728px; font-family: "Raleway", sans-serif; font-weight: 200; font-size: 38px; color: var(--grey-mid); letter-spacing: 3px; }

  .panel { position: absolute; top: 778px; height: 207px; }
  .panel--greater-good { left: 40px; width: 172px; background: var(--panel-dark); }
  .panel--serve-people { left: 216px; width: 162px; background: var(--panel-light); }

  .service-big { top: 12px; font-family: "Oswald", sans-serif; font-weight: 500; font-size: 50px; color: var(--paper); letter-spacing: -1px; }
  .is-for-the { top: 76px; font-family: "Roboto Slab", serif; font-weight: 300; font-size: 23px; color: var(--ink); }
  .greater { top: 104px; font-family: "Roboto Slab", serif; font-weight: 700; font-size: 26px; color: #7a7a7a; }
  .good { top: 140px; font-family: "Raleway", sans-serif; font-weight: 200; font-size: 38px; color: var(--red); letter-spacing: 4px; }
  .o-heart { position: relative; display: inline-block; }
  .o-heart::after { content: "\2665"; position: absolute; left: 0; right: 0; top: 50%; transform: translateY(-50%);
    font-family: "Lato", sans-serif; font-size: 14px; text-align: center; color: var(--red); }

  .purpose { top: 12px; font-family: "Roboto Slab", serif; font-weight: 800; font-size: 29px; color: var(--ink-soft); letter-spacing: -1px; }
  .always { top: 46px; font-family: "Lato", sans-serif; font-size: 10px; color: var(--grey-mid); letter-spacing: 8px; padding-left: 8px; }
  .panel--serve-people .small-dot { top: 64px; }
  .serve { top: 86px; font-family: "Raleway", sans-serif; font-weight: 200; font-size: 46px; color: var(--ink); letter-spacing: 2px; }
  .people { top: 148px; font-family: "Lato", sans-serif; font-weight: 900; font-size: 35px; color: var(--red); }
</style>
</head>
<body>
<div class="canvas">
  <article class="manifesto" aria-label="Bright Lantern manifesto">
    <svg class="manifesto__frame" viewBox="0 0 418 1026" aria-hidden="true">
      <path fill="var(--red)" d="M0,76 L76,76 C100,10 160,0 209,0 C258,0 318,10 342,76 L418,76 L418,1026 L0,1026 Z"/>
      <path fill="var(--frame-grey)" d="M9,85 L83,85 C106,20 163,9 209,9 C255,9 312,20 335,85 L409,85 L409,1017 L9,1017 Z"/>
      <path fill="var(--paper)" d="M21,97 L92,97 C114,34 166,21 209,21 C252,21 304,34 326,97 L397,97 L397,1005 L21,1005 Z"/>
    </svg>

    <div class="line brand"><span class="brand__dot"></span>Bright Lantern</div>
    <div class="line brand__tagline">CARE · HEALING · COMMUNITY</div>

    <svg class="swoosh" viewBox="0 0 338 20" aria-hidden="true">
      <path d="M2,14 C80,2 140,18 169,10 C200,2 260,18 336,6" fill="none" stroke="var(--grey-light)" stroke-width="1.2"/>
    </svg>

    <div class="band band--left"></div>
    <div class="band band--right"></div>
    <div class="line we-are">WE ARE</div>

    <svg class="heart" viewBox="0 0 56 50" aria-hidden="true">
      <path fill="var(--red)" d="M28,48 C12,36 2,27 2,15 C2,7 8,2 15,2 C21,2 25,6 28,10 C31,6 35,2 41,2 C48,2 54,7 54,15 C54,27 44,36 28,48 Z"/>
    </svg>
    <div class="heart__letter">A</div>

    <h1 class="line for-purpose">FOR-PURPOSE</h1>
    <div class="line organisation">ORGANISATION</div>

    <div class="dotted dotted--upper"></div>
    <div class="line every-large">EVERY</div>
    <div class="dotted dotted--lower"></div>

    <section class="column column--service">
      <div class="line service-title">SERVICE</div>
      <div class="line we-offer">we offer</div>
      <svg class="ribbon" viewBox="0 0 140 28" aria-hidden="true">
        <path d="M2,4 L24,4 L24,24 L2,24 L10,14 Z M138,4 L116,4 L116,24 L138,24 L130,14 Z" fill="none" stroke="var(--grey-light)" stroke-width="1.2"/>
        <rect x="20" y="1" width="100" height="26" fill="var(--paper)" stroke="var(--grey-light)" stroke-width="1.2"/>
      </svg>
      <div class="line ribbon__word">FREE</div>
      <div class="rule"></div>
      <div class="every-band">EVERY</div>
      <div class="line financial">financial</div>
      <div class="line transaction">TRANSACTION</div>
      <div class="small-dot">is</div>
      <div class="line transparent">TRANSPARENT</div>
    </section>

    <section class="column column--product">
      <div class="line product-title">PRODUCT</div>
      <div class="line we-sell">we sell</div>
      <div class="line funds">FUNDS</div>
      <div class="line our-small">OUR</div>
      <div class="line services">SERVICES</div>
    </section>

    <svg class="chevron" viewBox="0 0 338 62" aria-hidden="true">
      <polygon points="0,0 169,32 338,0 338,62 0,62" fill="var(--panel-light)"/>
      <polyline points="0,0 169,32 338,0" fill="none" stroke="var(--grey-light)" stroke-width="1.5"/>
    </svg>
    <div class="line our-divider">OUR</div>

    <section class="panel panel--greater-good">
      <div class="line service-big">SERVICE</div>
      <div class="line is-for-the">is for the</div>
      <div class="line greater">greater</div>
      <div class="line good">G<span class="o-heart">O</span><span class="o-heart">O</span>D</div>
    </section>

    <section class="panel panel--serve-people">
      <div class="line purpose">PURPOSE</div>
      <div class="line always">ALWAYS</div>
      <div class="small-dot">to</div>
      <div class="line serve">SERVE</div>
      <div class="line people">PEOPLE</div>
    </section>
  </article>
</div>
</body>
</html>
```